Wedding invitation

We need a wedding invitation designed with a logo using our initials and name underneath.
We are getting married at THE BRENNA hotel in Gstaad and we would like have our logo similar to theirs but incorporating our initials n&g (any font/case) and our names below noreen and Gilberto. THE BRENNA logo can be seen on their website.
The invitation would be square with the logo on the front in stamped foil and the colour would be THE BRENNA brown (I have the exact colour)
THE BRENNA Brown: C45 M70 Y68 K77
THE BRENNA Rose Gold: VELMAR 218
Inside we would have the invitation wording and on the opposite side some contact info. There would be four inserts - accom, directions, brunch and RSVP. We will provide the wording.

```html
<!DOCTYPE html>
<html lang="en">
<head>
<meta charset="utf-8">
<title>RSVP Card</title>
<link rel="stylesheet" href="https://fonts.googleapis.com/css2?family=Alex+Brush&family=Lora:ital@0;1&display=swap">
<style>
  :root {
    --rose: #b46c77;
    --rose-soft: #e9c9ce;
    --brown: #2e1a16;
    --paper: #ffffff;
  }
  html, body {
    margin: 0;
    padding: 0;
    width: 1200px;
    height: 1200px;
    overflow: hidden;
    background: var(--paper);
  }
  .rsvp-card {
    display: block;
    width: 1200px;
    height: 1200px;
  }
  .frame-line { stroke: var(--rose); stroke-width: 2.2; fill: none; }
  .card-title {
    font-family: "Alex Brush", cursive;
    font-size: 96px;
    fill: var(--brown);
  }
  .name-initial {
    font-family: "Alex Brush", cursive;
    font-size: 62px;
    fill: var(--brown);
  }
  .ampersand {
    font-family: "Lora", serif;
    font-size: 42px;
    fill: var(--rose);
  }
  .name-dots {
    stroke: var(--brown);
    stroke-width: 3;
    stroke-linecap: round;
    stroke-dasharray: 0 6.4;
  }
  .choice-ring { fill: none; stroke: var(--rose); stroke-width: 3.4; }
  .choice-label {
    font-family: "Lora", serif;
    font-size: 27px;
    fill: var(--rose);
  }
  .field-label {
    font-family: "Lora", serif;
    font-size: 21px;
    fill: var(--rose);
  }
  .field-dots {
    stroke: var(--rose);
    stroke-width: 2.4;
    stroke-linecap: round;
    stroke-dasharray: 0 4.4;
  }
  .respond-note {
    font-family: "Lora", serif;
    font-style: italic;
    font-size: 22px;
    fill: var(--rose);
  }
</style>
</head>
<body>
<svg class="rsvp-card" viewBox="0 0 900 900" xmlns="http://www.w3.org/2000/svg">
  <defs>
    <radialGradient id="ornamentTone" cx="50%" cy="50%" r="60%">
      <stop offset="0%" stop-color="#d9a5ad"/>
      <stop offset="100%" stop-color="#f6e6e9"/>
    </radialGradient>
    <linearGradient id="flourishTone" x1="0" x2="1" y1="0" y2="0">
      <stop offset="0%" stop-color="#f6e6e9"/>
      <stop offset="50%" stop-color="#d9a5ad"/>
      <stop offset="100%" stop-color="#f6e6e9"/>
    </linearGradient>
  </defs>

  <!-- double frame -->
  <g class="card-frame">
    <line class="frame-line" x1="148" y1="18" x2="750" y2="18"/>
    <line class="frame-line" x1="148" y1="23.5" x2="750" y2="23.5"/>
    <line class="frame-line" x1="148" y1="873" x2="750" y2="873"/>
    <line class="frame-line" x1="148" y1="878.5" x2="750" y2="878.5"/>
    <line class="frame-line" x1="18" y1="148" x2="18" y2="752"/>
    <line class="frame-line" x1="23.5" y1="148" x2="23.5" y2="752"/>
    <line class="frame-line" x1="876.5" y1="148" x2="876.5" y2="752"/>
    <line class="frame-line" x1="882" y1="148" x2="882" y2="752"/>
  </g>

  <!-- corner ornaments -->
  <g class="corner-ornaments">
    <rect x="16" y="14" width="128" height="128" rx="30" fill="url(#ornamentTone)" opacity="0.55" role="img" aria-label="Scrolled filigree corner ornament, top left"/>
    <rect x="756" y="14" width="128" height="128" rx="30" fill="url(#ornamentTone)" opacity="0.55" role="img" aria-label="Scrolled filigree corner ornament, top right"/>
    <rect x="16" y="756" width="128" height="128" rx="30" fill="url(#ornamentTone)" opacity="0.55" role="img" aria-label="Scrolled filigree corner ornament, bottom left"/>
    <rect x="756" y="756" width="128" height="128" rx="30" fill="url(#ornamentTone)" opacity="0.55" role="img" aria-label="Scrolled filigree corner ornament, bottom right"/>
  </g>

  <!-- heading -->
  <text class="card-title" x="432" y="156" text-anchor="middle">RSVP</text>
  <rect x="272" y="184" width="298" height="44" rx="22" fill="url(#flourishTone)" opacity="0.7" role="img" aria-label="Looped scroll flourish divider"/>

  <!-- guest names -->
  <g class="guest-line">
    <text class="name-initial" x="80" y="362">M</text>
    <line class="name-dots" x1="136" y1="360" x2="795" y2="360"/>
  </g>
  <g class="guest-line">
    <text class="ampersand" x="78" y="456">&amp;</text>
    <text class="name-initial" x="130" y="456">M</text>
    <line class="name-dots" x1="186" y1="454" x2="808" y2="454"/>
  </g>

  <!-- response choices -->
  <g class="response-choice">
    <circle class="choice-ring" cx="106" cy="571" r="22"/>
    <text class="choice-label" x="138" y="582">Accepts with pleasure</text>
  </g>
  <g class="response-choice">
    <circle class="choice-ring" cx="517" cy="571" r="22"/>
    <text class="choice-label" x="549" y="581">Declines with regrets</text>
  </g>

  <!-- dietary -->
  <text class="field-label" x="80" y="685">Dietary Requirements</text>
  <line class="field-dots" x1="82" y1="746" x2="812" y2="746"/>

  <!-- deadline -->
  <text class="respond-note" x="444" y="835" text-anchor="middle">Kindly respond by.....March 2014</text>
</svg>
</body>
</html>
```